Gymnastics Award Design Needed--for kids

Need a gymnastics certificate or award designed. Will be printed on a piece of 8.5x11 paper. The award will be celebrating the gymnast learning a new skill in gymnastics. So it should be fun, but still look "official". Needs to look good hanging on a gymnast's bedroom wall.

It should say "The Aerial Cartwheel Club"
I will be using this design to change it based on the skill.

My main colors are:
#34475D
#E1467A
#7555A4

So should use those, but can add others

My website is tumblenest.net so you can see the look/feel.

Target Market(s)

Main audience will be girls ages 5-12, but will also be used by slightly older girls and boys. So needs to be fun, not too gender specific.

Industry/Entity Type

Learning

Requirements
Must have
• The following will need to go on the certificate:
• * Name of Skill
• * Image of Skill
• * Gymnast's Name
• * my logo
• * Gym's Logo
• * Gym's Name
• Optional: Date

```html
<!DOCTYPE html>
<html lang="en">
<head>
<meta charset="utf-8">
<title>The Aerial Cartwheel Club – Award Certificate</title>
<link rel="stylesheet" href="https://fonts.googleapis.com/css2?family=Anton&family=Yellowtail&family=Roboto+Condensed:wght@400&display=swap">
<style>
  :root {
    --violet: #5b3dff;
    --paper: #ffffff;
    --ink: #111111;
    --mist: #e6e6e6;
    --blush: #f5b6e6;
    --rose: #e8389a;
  }
  html, body {
    margin: 0;
    padding: 0;
    width: 1200px;
    height: 848px;
    overflow: hidden;
    background: var(--paper);
  }
  .certificate {
    position: relative;
    width: 1200px;
    height: 848px;
    overflow: hidden;
    font-family: "Roboto Condensed", "Arial Narrow", sans-serif;
    color: var(--ink);
  }
  .frame { position: absolute; inset: 0; }
  .backdrop-figure {
    position: absolute;
    top: 292px;
    width: 388px;
    height: 380px;
    background: linear-gradient(180deg, var(--mist), rgba(230,230,230,0.55));
    border-radius: 48% 48% 12px 12px;
  }
  .backdrop-figure.left { left: 28px; }
  .backdrop-figure.right { left: 576px; }
  .skill-pose {
    position: absolute;
    left: 1002px;
    width: 124px;
    height: 120px;
    background: var(--blush);
    border-radius: 14px;
  }
  .headline { position: absolute; left: 0; top: 0; }
  .field {
    position: absolute;
    text-align: center;
    font-size: 37px;
    line-height: 1;
    white-space: nowrap;
  }
  .dotted {
    position: absolute;
    height: 0;
    border-bottom: 2px dotted var(--ink);
  }
  .gym-mark {
    position: absolute;
    left: 74px;
    top: 682px;
    width: 220px;
    display: flex;
    flex-direction: column;
    align-items: center;
    gap: 12px;
  }
  .gym-mark .dot {
    width: 56px;
    height: 56px;
    border-radius: 50%;
    background: var(--violet);
  }
  .gym-mark .name {
    font-size: 28px;
    letter-spacing: 1px;
  }
  .date {
    position: absolute;
    left: 380px;
    top: 756px;
    font-size: 24px;
  }
  .date .blank {
    display: inline-block;
    width: 150px;
    border-bottom: 2px dotted var(--ink);
    margin-left: 6px;
  }
  .partner-mark {
    position: absolute;
    left: 664px;
    top: 742px;
    display: flex;
    align-items: center;
    gap: 12px;
  }
  .partner-mark .dot {
    width: 36px;
    height: 36px;
    border-radius: 50%;
    background: var(--violet);
  }
  .partner-mark .name {
    font-size: 36px;
    color: var(--rose);
    letter-spacing: 1px;
  }
</style>
</head>
<body>
<main class="certificate">
  <svg class="frame" width="1200" height="848" viewBox="0 0 1200 848" aria-hidden="true">
    <rect width="1200" height="848" fill="var(--violet)"/>
    <polygon fill="var(--paper)" points="6,150 150,6 982,6 982,842 150,842 6,698"/>
    <circle cx="78" cy="78" r="48" fill="var(--violet)"/>
    <circle cx="78" cy="770" r="48" fill="var(--violet)"/>
    <rect x="1146" y="6" width="12" height="836" fill="var(--paper)"/>
    <rect x="1180" y="6" width="12" height="836" fill="var(--paper)"/>
  </svg>

  <div class="backdrop-figure left" role="img" aria-label="Faint grey silhouette of a gymnast bending into a backbend"></div>
  <div class="backdrop-figure right" role="img" aria-label="Faint grey silhouette of a gymnast bending into a backbend, mirrored"></div>

  <div class="skill-pose" style="top:116px" role="img" aria-label="Pink silhouette of a gymnast in a split leap"></div>
  <div class="skill-pose" style="top:280px" role="img" aria-label="Pink silhouette of a gymnast in a side bend"></div>
  <div class="skill-pose" style="top:436px" role="img" aria-label="Pink silhouette of a gymnast in a floor back arch"></div>
  <div class="skill-pose" style="top:582px;height:146px" role="img" aria-label="Pink silhouette of a gymnast in a standing needle scale"></div>

  <svg class="headline" width="982" height="320" viewBox="0 0 982 320">
    <text x="196" y="150" font-family="Yellowtail, cursive" font-size="74" fill="var(--ink)">The</text>
    <text x="324" y="152" font-family="Anton, Impact, sans-serif" font-size="132" fill="var(--violet)" textLength="372" lengthAdjust="spacingAndGlyphs">AERIAL</text>
    <text x="184" y="292" font-family="Anton, Impact, sans-serif" font-size="134" fill="var(--violet)" textLength="656" lengthAdjust="spacingAndGlyphs">CARTWHEEL</text>
    <text x="808" y="248" font-family="Yellowtail, cursive" font-size="86" fill="var(--ink)" stroke="var(--paper)" stroke-width="4" paint-order="stroke">Club</text>
  </svg>

  <div class="field" style="left:296px;width:430px;top:358px">Name of Skill</div>
  <div class="dotted" style="left:296px;width:430px;top:400px"></div>

  <div class="field" style="left:198px;width:626px;top:478px">Presented To:</div>
  <div class="dotted" style="left:198px;width:626px;top:571px"></div>

  <div class="field" style="left:198px;width:626px;top:614px">by Maple Gymnastics Gym.</div>

  <div class="gym-mark">
    <span class="dot"></span>
    <span class="name">Maple Gym</span>
  </div>

  <div class="date">Date:<span class="blank"></span></div>

  <div class="partner-mark">
    <span class="dot"></span>
    <span class="name">TUMBLE NEST</span>
  </div>
</main>
</body>
</html>
```